Demo, Strip out Rubbish and Asbestos Removal

we need a business card to give to clients to provide information about our Demo Strip out rubbish and Asbestos removal as well as labour hire.
I was thinking of a silhouette of a tip truck with the services we provide being dumped out the back in bullet form.
KB in a green colour and Refuse in a grey colour.
Greens, greys, blacks, white, silvers, matt grey. But am very open to other colour schemers and designs. I do like the tough of a matt card with gloss writing or vies versa.
We are also looking to use this design as our logo

Target Market(s)

builders - commercial residential . General public

Industry/Entity Type

Business

Contact Information for Business Card

KB Refuse
Dean Harlow
0471203658
kbrefuse@mailvista.example

Font styles to use
Sans Serif

Colors
9bcb3c
00a990
0355a3
000000
5c5c5c
cbcbcb
fbee3f
ffffff
ffcf3e

Requirements
Must have
• Abn: 57219038446
Nice to have
• bullet form
:demo and strip out
:asbestos and rubbishe removal
:labour hire
:Residential and commercial clean up
:yard clearing

```html
<!DOCTYPE html>
<html lang="en">
<head>
<meta charset="utf-8">
<title>KB Refuse Business Card</title>
<link href="https://fonts.googleapis.com/css2?family=Questrial&display=swap" rel="stylesheet">
<style>
  :root {
    --page: #e9ebea;
    --card-white: #ffffff;
    --mint: #c9ecd7;
    --mint-deep: #b3e3c7;
    --green: #1fa64a;
    --grey-text: #4a4a4a;
    --rule: #1b1b1b;
    --bullet: #9fd6b5;
    --truck-light: #d9d9d9;
    --truck-dark: #6a6a6a;
  }
  * { box-sizing: border-box; margin: 0; padding: 0; }
  html, body { width: 1200px; height: 1000px; overflow: hidden; }
  body {
    background: var(--page);
    font-family: "Questrial", sans-serif;
    display: flex;
    flex-direction: column;
    align-items: center;
    justify-content: center;
    gap: 60px;
  }
  .card {
    position: relative;
    width: 700px;
    height: 400px;
    overflow: hidden;
    background:
      radial-gradient(ellipse 75% 70% at 50% 55%, var(--mint-deep) 0%, var(--mint) 55%, rgba(201,236,215,0.35) 80%, var(--card-white) 100%);
    box-shadow: 0 6px 18px rgba(0,0,0,0.18);
  }
  /* Front */
  .card-front .brand {
    position: absolute;
    top: 70px;
    left: 0;
    width: 100%;
    display: flex;
    justify-content: center;
    align-items: center;
    gap: 14px;
    font-size: 62px;
    letter-spacing: 1px;
    color: var(--green);
  }
  .brand .mark {
    width: 22px;
    height: 22px;
    background: var(--green);
  }
  .card-front .holder {
    position: absolute;
    top: 185px;
    left: 50%;
    transform: translateX(-50%);
    width: 230px;
    padding: 10px 0;
    text-align: center;
    font-size: 28px;
    color: var(--grey-text);
    border-top: 1px solid rgba(0,0,0,0.12);
    border-bottom: 1px solid rgba(0,0,0,0.12);
  }
  .card-front .contacts {
    position: absolute;
    top: 272px;
    left: 0;
    width: 100%;
    list-style: none;
    text-align: center;
    font-size: 19px;
    color: var(--grey-text);
    line-height: 1.4;
  }
  .contacts .abn { font-size: 16px; margin-top: 4px; }
  .contacts .icon { width: 16px; height: 16px; vertical-align: -2px; margin-right: 6px; }
  /* Back */
  .card-back .truck {
    position: absolute;
    left: 30px;
    top: 170px;
    width: 250px;
    height: 230px;
    border-radius: 6px 30px 0 0;
    background: linear-gradient(160deg, var(--truck-light) 0%, #a8a8a8 55%, var(--truck-dark) 100%);
    opacity: 0.85;
  }
  .card-back .services {
    position: absolute;
    top: 60px;
    left: 250px;
    list-style: none;
    font-size: 20px;
    color: var(--grey-text);
  }
  .services li { position: relative; padding-left: 22px; margin-bottom: 24px; }
  .services li:nth-child(2) { margin-left: 55px; }
  .services li:nth-child(3) { margin-left: 110px; }
  .services li::before {
    content: "";
    position: absolute;
    left: 0; top: 8px;
    width: 9px; height: 9px;
    border-radius: 50%;
    background: var(--bullet);
  }
  .card-back .brand-small {
    position: absolute;
    right: 40px;
    top: 302px;
    font-size: 24px;
    color: var(--green);
  }
  .card-back .rule {
    position: absolute;
    left: 290px;
    right: 0;
    top: 340px;
    height: 2px;
    background: var(--rule);
  }
</style>
</head>
<body>
  <section class="card card-front">
    <div class="brand"><span class="mark" aria-hidden="true"></span>KB Refuse</div>
    <div class="holder">Dean Harlow</div>
    <ul class="contacts">
      <li>
        <svg class="icon" viewBox="0 0 24 24" aria-hidden="true"><path fill="#1fa64a" d="M6.6 10.8a15 15 0 0 0 6.6 6.6l2.2-2.2a1 1 0 0 1 1-.25 11.4 11.4 0 0 0 3.6.57 1 1 0 0 1 1 1V20a1 1 0 0 1-1 1A17 17 0 0 1 3 4a1 1 0 0 1 1-1h3.5a1 1 0 0 1 1 1c0 1.25.2 2.45.57 3.57a1 1 0 0 1-.25 1z"/></svg>0471203658
      </li>
      <li>
        <svg class="icon" viewBox="0 0 24 24" aria-hidden="true"><rect x="2" y="5" width="20" height="14" fill="#1fa64a"/><path d="M2 5l10 8 10-8" fill="none" stroke="#c9ecd7" stroke-width="1.6"/></svg>kbrefuse@mailvista.example
      </li>
      <li class="abn">ABN 57219038446</li>
    </ul>
  </section>

  <section class="card card-back">
    <div class="truck" role="img" aria-label="Grey tip truck illustration tipping its tray"></div>
    <ul class="services">
      <li>Demo / strip outs</li>
      <li>Rubbish and asbestos removal</li>
      <li>Labour hire</li>
    </ul>
    <div class="brand-small">KB Refuse</div>
    <div class="rule"></div>
  </section>
</body>
</html>
```